Foundation needs poster to represent $1 billion goal with 3 comma concept

We need a poster created to serve as an aspirational reminder of our efforts to reach $1billion in assets. In pop culture, the term "3 commas" has become slang for being part of an exclusive 1,000,000,000 club. The poster should not explicitly say "3 comma club", but should have 3 commas (", , ,") as a primary focal point. The poster is meant to be more of an art/discussion piece than actually communicate any specific information - more abstract than literal. Colors should be black, white, maroon (R140-G29-B64), and/or gold (255-198-39). Font should be Akzidenz Grotesk Standard. If thats not available, Roboto or Helvetica Neue will work too. The attached file is an image of a hand with 3 fingers up - it can, but does not need to be incorporated into the design.

Industry/Entity Type

Finance

Font styles to use
Sans Serif

Requirements
Must have
• , , ,
• Use of Maroon and Gold colors
Nice to have
• Stock market and financial market symbols (things like euro, yen, pound symbols) as background or secondary.
Should not have
• Should not explicitly say club or billion

```html
<!DOCTYPE html>
<html lang="en">
<head>
<meta charset="utf-8">
<title>Three Commas Poster</title>
<link rel="stylesheet" href="https://fonts.googleapis.com/css2?family=Montserrat:wght@300;400&display=swap">
<style>
  :root {
    --backdrop: #e8e8eb;
    --paper: #fafafa;
    --maroon: #c01f40;
    --gold: #fdc41d;
    --gold-light: #fde08a;
    --gold-deep: #e9a92a;
    --bronze: #8a6235;
    --chart-red: #d9553a;
    --figure-white: #ffffff;
  }
  html, body {
    margin: 0;
    padding: 0;
    width: 1200px;
    height: 839px;
    overflow: hidden;
    background: var(--backdrop);
  }
  .canvas {
    position: relative;
    width: 1200px;
    height: 839px;
  }
  .poster {
    position: absolute;
    left: 305px;
    top: 30px;
    width: 590px;
    height: 780px;
    background: var(--paper);
    box-shadow: 0 4px 18px rgba(0, 0, 0, 0.12);
    overflow: hidden;
  }
  .poster svg {
    display: block;
    width: 590px;
    height: 780px;
  }
  .figure {
    font-family: "Montserrat", "Helvetica Neue", sans-serif;
    font-weight: 300;
    fill: var(--figure-white);
    fill-opacity: 0.85;
  }
  .figure--large { font-size: 28px; }
  .figure--medium { font-size: 23px; }
  .figure--small { font-size: 11px; }
  .figure--stack { font-size: 12px; }
  .comma {
    fill: var(--maroon);
    stroke: var(--figure-white);
    stroke-width: 7;
    paint-order: stroke;
    stroke-linejoin: round;
  }
  .growth-line {
    fill: none;
    stroke: var(--chart-red);
    stroke-width: 10;
    stroke-linejoin: miter;
    stroke-opacity: 0.72;
  }
  .growth-head { fill: var(--chart-red); fill-opacity: 0.72; }
</style>
</head>
<body>
<main class="canvas">
  <article class="poster">
    <svg viewBox="0 0 590 780" xmlns="http://www.w3.org/2000/svg">
      <defs>
        <linearGradient id="swash-fill" x1="0" y1="0" x2="0" y2="1">
          <stop offset="0" stop-color="var(--gold)"/>
          <stop offset="0.45" stop-color="var(--gold-light)"/>
          <stop offset="0.7" stop-color="var(--gold-deep)"/>
          <stop offset="1" stop-color="var(--bronze)"/>
        </linearGradient>
      </defs>

      <path class="market-swash" role="img"
            aria-label="Gold paint brush sweep with a city skyline and market bar chart"
            fill="url(#swash-fill)"
            d="M590,160 L590,780 L0,780 L0,650 C40,580 120,530 240,505 C370,450 480,330 590,160 Z"/>

      <rect class="pointing-hand" role="img"
            aria-label="Gold cartoon hand reaching down with three fingers extended"
            x="231" y="0" width="127" height="303" rx="22"
            fill="var(--gold)" stroke="#7a7a7a" stroke-width="3"/>

      <g class="commas">
        <path class="comma" d="M131,381 a53,53 0 1,1 106,0 C238,450 200,505 145,540 L137,520 C175,495 195,465 192,432 C162,440 131,420 131,381 Z"/>
        <path class="comma" d="M233,381 a53,53 0 1,1 106,0 C340,450 302,505 247,540 L239,520 C277,495 297,465 294,432 C264,440 233,420 233,381 Z"/>
        <path class="comma" d="M341,381 a53,53 0 1,1 106,0 C448,450 410,505 355,540 L347,520 C385,495 405,465 402,432 C372,440 341,420 341,381 Z"/>
      </g>

      <g class="growth-chart">
        <polyline class="growth-line"
                  points="151,619 173,591 184,608 209,713 306,575 336,641 347,619 361,669 428,613 442,621 490,540"/>
        <polygon class="growth-head" points="505,522 476,532 498,553"/>
      </g>

      <g class="market-figures">
        <text class="figure figure--large" x="464" y="605">+9.11%</text>
        <text class="figure figure--medium" x="256" y="685">15.18%</text>
        <text class="figure figure--small" x="375" y="657">+2.199%</text>
        <text class="figure figure--medium" x="472" y="738">+4.34%</text>

        <text class="figure figure--stack" x="116" y="602">
          <tspan x="116" dy="0">.358/</tspan>
          <tspan x="116" dy="14">.125</tspan>
          <tspan x="116" dy="14">1.985</tspan>
          <tspan x="116" dy="14">2.587</tspan>
        </text>
        <text class="figure figure--stack" x="473" y="622">
          <tspan x="473" dy="0">.358/</tspan>
          <tspan x="473" dy="14">.125</tspan>
          <tspan x="473" dy="14">1.985</tspan>
          <tspan x="473" dy="14">2.587</tspan>
        </text>
        <text class="figure figure--stack" x="148" y="694">
          <tspan x="148" dy="0">.358/</tspan>
          <tspan x="148" dy="14">.125</tspan>
          <tspan x="148" dy="14">1.985</tspan>
          <tspan x="148" dy="14">2.587</tspan>
        </text>
      </g>
    </svg>
  </article>
</main>
</body>
</html>
```